Etiketten für Kosmetik Produkte  100% Natural Made in Germany
Etiketten für Kosmetik Produkte 100% Natural Made in Germany
Zielgruppe
auf Hochwertige -zertifizierte Naturprodukte wert legen.
Hergestellt in Deutschland und Verpackt
Aufgabenstellung
Hallo ihr lieben,
für die SilberTau Kosmetik - wünschen wir einen neuen frischen Style - das dunkle Etikett möchten wir los werden.
Ein helles frisches Design
Zielgruppe- alle die auf Hochwertige - zertifizierte Naturprodukte bevorzugen
Die Produkte haben mit eine BRENO Zertifizierung - Höchste Qalität an Naturprodukte
Das Glas was wir nutzen ist ein violettes Glas und sehr hochwertig was wir beibehalten möchten.
Das Produkt ist dadurch sehr Geschütz und nachhaltig dazu
Es sind 12 Produkte - Design bleibt bei allen gleich.
Design Wunsch -!!!!
Was gut zum Glas Passt- nur kein schwarz bitte
und Produkt gut passt
Weiß - Kupfer eventuell
Kein Muss - sind für alles offen ( nur kein schwarz
Logo - Name bleibt :-)
Das Design von Telvira Naturkosmetik
Gefällt uns sehr gut in der Richtung
Was die Natürlichkeit- Reinheit - Qualität
Verkörpert:-)
Fotos zum Prosukt:
Hier ein link zum Instagram
https://instagram.com/murelio.iberia?igshid=MzRlODBiNWFlZA==
https://instagram.com/silbertau_naturkosmetik?igshid=MzRlODBiNWFlZA==
An den Flyer den wir hochgeladen kann man sehen um welche Produkte es sich handelt und auch im Instagram zu sehen sind.
Wenn ihr weitere Fotos benötigen tut- bitte melden
Viel Glück :-) danke für eure Unterstützung

```html
<!DOCTYPE html>
<html lang="de">
<head>
<meta charset="utf-8">
<title>SilberTau Naturkosmetik – Allrounder Cream Etikett</title>
<link rel="stylesheet" href="https://fonts.googleapis.com/css2?family=Cinzel:wght@400&family=Montserrat:wght@400;500;700&display=swap">
<style>
  :root {
    --glass-violet: #1c0649;
    --label-cream: #e3ddd0;
    --copper-deep: #8f6226;
    --copper-mid: #ac7c36;
    --copper-light: #c49a55;
    --gold-pale: #d6c8a6;
    --gold-paler: #ddd2b8;
    --text-gold: #8f6427;
  }
  * { margin: 0; padding: 0; box-sizing: border-box; }
  html, body {
    width: 1200px; height: 1200px; overflow: hidden;
    background: var(--glass-violet);
  }
  .label { position: relative; width: 1200px; height: 1200px; }
  .label-art { position: absolute; inset: 0; }
  .brand {
    position: absolute; left: 0; right: 0; top: 120px;
    text-align: center; color: var(--text-gold);
    font-family: "Cinzel", serif; font-weight: 400;
    padding-left: 28px;
  }
  .brand-mark {
    width: 74px; height: 74px; margin: 0 auto 14px;
    border: 2px solid var(--text-gold); border-radius: 50%;
  }
  .brand-name { font-size: 50px; line-height: 1; letter-spacing: 0.02em; }
  .brand-sub { font-size: 25px; line-height: 1; margin-top: 4px; letter-spacing: 0.03em; }
  .product-name {
    position: absolute; left: 0; right: 0; top: 449px;
    text-align: center; padding-left: 26px;
    font-family: "Montserrat", sans-serif; font-weight: 500;
    font-size: 32px; line-height: 1; letter-spacing: 0.08em; color: var(--text-gold);
  }
  .category {
    position: absolute; left: 0; right: 0; top: 795px;
    text-align: center; padding-left: 44px;
    font-family: "Montserrat", sans-serif; font-weight: 700;
    font-size: 31px; line-height: 1; letter-spacing: 0.03em; color: var(--text-gold);
  }
  .quality {
    position: absolute; left: 0; right: 0; top: 855px;
    text-align: center; padding-left: 44px;
    font-family: "Montserrat", sans-serif; font-weight: 400;
    font-size: 23px; line-height: 1; letter-spacing: 0.06em; color: var(--text-gold);
  }
</style>
</head>
<body>
<main class="label">
  <svg class="label-art" width="1200" height="1200" viewBox="0 0 1200 1200">
    <defs>
      <clipPath id="label-disc"><circle cx="600" cy="600" r="570"/></clipPath>
      <radialGradient id="copper-glow" cx="0.5" cy="0.5" r="0.5">
        <stop offset="0" stop-color="var(--copper-light)"/>
        <stop offset="0.45" stop-color="var(--copper-mid)" stop-opacity="0.9"/>
        <stop offset="0.75" stop-color="var(--copper-deep)" stop-opacity="0.45"/>
        <stop offset="1" stop-color="var(--copper-deep)" stop-opacity="0"/>
      </radialGradient>
      <radialGradient id="pale-glow" cx="0.5" cy="0.5" r="0.5">
        <stop offset="0" stop-color="var(--gold-pale)"/>
        <stop offset="0.6" stop-color="var(--gold-paler)" stop-opacity="0.8"/>
        <stop offset="1" stop-color="var(--gold-paler)" stop-opacity="0"/>
      </radialGradient>
    </defs>
    <circle class="label-disc" cx="600" cy="600" r="570" fill="var(--label-cream)"/>
    <g clip-path="url(#label-disc)">
      <ellipse class="foliage-copper" role="img" aria-label="Stilisierte Blätterzweige in gebürstetem Kupfer auf der linken Seite"
        cx="290" cy="760" rx="330" ry="480" fill="url(#copper-glow)"/>
      <ellipse class="foliage-pale" role="img" aria-label="Stilisierte Blätterzweige in hellem gebürstetem Gold auf der rechten Seite"
        cx="910" cy="760" rx="330" ry="480" fill="url(#pale-glow)"/>
    </g>
  </svg>

  <header class="brand">
    <div class="brand-mark"></div>
    <div class="brand-name">SILBERTAU</div>
    <div class="brand-sub">NATURKOSMETIK</div>
  </header>

  <h1 class="product-name">ALLROUNDER CREAM</h1>
  <p class="category">FACIAL CARE</p>
  <p class="quality">ORGANIC</p>
</main>
</body>
</html>
```